New Internet Service provider for regional or isolated businesses

I'm looking for a logo and basic information website for an Internet company - "Quill Ridge Networks". This new company will be providing specialised Internet connectivity for isolated areas or where connectivity is too expensive for one business.
i.e Linking Workplaces as one for faster, cheaper Web access.
3 Types of Pages
1. Home Page
2. Content Page templates
3. More Information Form
1. Contact Name. 2. Business Address. 3. Business Phone Number. 4. Mobile Phone. 5. Number of Staff 6. Current Internet connection . 7. Speed 8. Comments ?
Web Pages
**Quill Ridge Networks **
Linking Workplaces as one for faster Web access
Who is Quill Ridge Networks ?
How do we work ?
Which carriers ?
Technologies Used ?
Contact details
Check my address now ?
(Form)
Our company will be using Fibre and Microwave/Radio technology to connect remote businesses to high speed Internet
Target Market(s)
Business customers with minimum 10 staff outside metropolitan areas
Industry/Entity Type
Internet Service Provider
Coding
Coded - Design and coding required
Number of Pages Required
3 page
Requirements
Must have
- 3 Types of Pages
- 1. Home Page
- 2. Content Page templates (See above)
- 3. "More Information" Form
- 1. Contact Name. 2. Business Address. 3. Business Phone Number. 4. Mobile Phone. 5. Number of Staff 6.Current Internet connection . 7. Speed 8.Comments ?
Nice to have
- Pictures of fibre optics, radio towers, stock photos of businesses / PC's
- Some ideas on the companies we will be using (I am looking for something similar in my website).
- In order of preference
- 1. www.travenlo.com.au
- 2. www.pomrika.com,au
- 3.www.fendoly.com.au

```html
<!DOCTYPE html>
<html lang="en">
<head>
<meta charset="utf-8">
<title>Quill Ridge Networks</title>
<link href="https://fonts.googleapis.com/css2?family=Roboto+Condensed:wght@400;700&family=Roboto:wght@400;500;700&display=swap" rel="stylesheet">
<style>
:root{
  --blue:#2b5aa8;
  --blue-dark:#1f4a92;
  --blue-band:#2c5fb0;
  --ink:#333;
  --muted:#666;
  --line:#ddd;
  --orange:#f47b20;
  --footer-bg:#f4f4f4;
  --dark:#2a2a2a;
}
*{margin:0;padding:0;box-sizing:border-box}
html,body{width:1200px;height:3061px;overflow:hidden}
body{position:relative;font-family:'Roboto',sans-serif;color:var(--ink);background:#fff}
.abs{position:absolute}
.cond{font-family:'Roboto Condensed',sans-serif}

/* header */
.site-header{left:0;top:0;width:1200px;height:100px;background:linear-gradient(#fff,#f1f1f1);border-bottom:3px solid #9aa3ad}
.brand{left:98px;top:24px;display:flex;align-items:center;gap:10px}
.brand-dot{width:48px;height:48px;border-radius:50%;background:var(--blue)}
.brand-name{font-family:'Roboto Condensed',sans-serif;font-weight:700;font-size:24px;line-height:1.05;color:var(--blue);width:150px}
.main-nav{left:565px;top:0;display:flex;height:97px}
.main-nav a{font-size:13px;color:#333;text-decoration:none;display:flex;align-items:center;padding:0 26px;height:97px}
.main-nav a.active{background:#fff;color:var(--blue);box-shadow:0 0 6px rgba(0,0,0,.15);border-bottom:3px solid var(--blue)}

/* hero */
.hero{left:0;top:100px;width:1200px;height:530px;background:linear-gradient(180deg,#7fb0cc 0%,#4f8fb3 45%,#2f6f95 70%,#c7b08e 100%)}
.hero-title{left:140px;top:190px;width:460px;text-align:center;color:#fff;font-family:'Roboto Condensed',sans-serif;text-shadow:0 2px 4px rgba(0,0,0,.3)}
.hero-title .l1{font-size:46px;text-transform:uppercase;line-height:1.1}
.hero-title .l2{font-size:40px;line-height:1.15}
.hero-arrow{top:318px}

/* welcome */
.section-title{font-family:'Roboto Condensed',sans-serif;font-size:31px;color:#333;text-transform:uppercase;text-align:center;width:1200px;left:0}
.intro{left:160px;top:746px;width:880px;text-align:center;font-size:11px;line-height:21px;color:var(--muted)}
.card{width:310px}
.card-media{height:176px;border:1px solid var(--line)}
.card h3{font-family:'Roboto Condensed',sans-serif;font-weight:400;font-size:17px;color:var(--blue);margin:24px 0 8px;text-transform:uppercase}
.card p{font-size:11px;line-height:20px;color:var(--muted)}
.more{display:inline-block;margin-top:16px;font-size:11px;color:var(--blue);font-weight:500;text-transform:uppercase}

/* connect band */
.connect{left:0;top:1224px;width:1200px;height:507px;background:linear-gradient(135deg,#3466b7,#2856a3 60%,#2a5ba9)}
.connect .section-title{color:#fff;top:62px}
.feature{width:330px;color:#fff}
.feature h4{font-family:'Roboto Condensed',sans-serif;font-weight:400;font-size:17px;text-transform:uppercase;margin-bottom:12px}
.feature p{font-size:11px;line-height:20px;color:#dfe8f7}
.icon-disc{width:122px;height:122px;border-radius:50%;background:#fff;display:flex;align-items:center;justify-content:center}

/* carriers */
.carrier-head{left:98px;top:1805px;display:flex;align-items:center;gap:14px}
.carrier-head .mark{width:52px;height:52px;border-radius:50%;background:#333}
.carrier-head h2{font-family:'Roboto Condensed',sans-serif;font-weight:400;font-size:31px;text-transform:uppercase;line-height:1}
.carrier-head .sub{font-size:15px;color:var(--blue);margin-top:4px}
.carrier-text{left:98px;top:1886px;width:550px;font-size:11px;line-height:20px;color:var(--muted)}
.carrier-text p+p{margin-top:12px}
.btn-blue{left:98px;top:2038px;width:112px;height:34px;background:var(--blue);color:#fff;font-size:11px;display:flex;align-items:center;justify-content:center;border-radius:2px}
.video{left:683px;top:1801px;width:417px;height:260px;background:linear-gradient(180deg,#fafafa,#e9e9e9 75%,#c9c9c9);border:1px solid #e3e3e3}
.video-shadow{left:690px;top:2064px;width:403px;height:14px;background:radial-gradient(ellipse at center,rgba(0,0,0,.35),rgba(0,0,0,0) 70%)}
.partner{top:2166px;width:159px;height:78px;border:1px solid var(--line);display:flex;align-items:center;justify-content:center}
.partner span{width:90px;height:22px;background:#cfcfcf;border-radius:2px}

/* booking */
.booking{left:0;top:2297px;width:1200px;height:410px;background:linear-gradient(135deg,#3a3a3a,#262626 50%,#33302c)}
.booking .section-title{color:#fff;font-size:40px;top:86px}
.field{width:276px;height:45px;background:#fff;font-size:11px;color:#555;font-style:italic;padding:0 12px;display:flex;align-items:center}
.btn-orange{background:var(--orange);color:#fff;font-style:normal;font-weight:700;font-size:14px;justify-content:center;text-transform:uppercase}

/* footer */
.site-footer{left:0;top:2707px;width:1200px;height:292px;background:var(--footer-bg)}
.f-col h5{font-family:'Roboto Condensed',sans-serif;font-weight:400;font-size:16px;text-transform:uppercase;color:#333;margin-bottom:14px}
.f-col p,.f-col li{font-size:11px;line-height:18px;color:#444}
.f-col ul{list-style:none}
.f-col li{line-height:22px}
.input{width:242px;height:40px;border:1px solid var(--line);background:#fff;font-size:11px;padding:0 14px;display:flex;align-items:center;margin-top:18px}
.btn-sub{width:102px;height:38px;background:var(--blue);color:#fff;font-size:11px;display:flex;align-items:center;justify-content:center;margin-top:10px;text-transform:uppercase}
.contact-row{display:flex;gap:12px;align-items:flex-start;margin-bottom:14px}
.socials{display:flex;gap:6px;margin-top:4px}
.socials span{width:22px;height:22px;background:var(--blue)}
.foot-brand{left:922px;top:2808px;display:flex;align-items:center;gap:10px}
.foot-brand .brand-dot{width:54px;height:54px}
.foot-brand .brand-name{font-size:27px;width:170px}
.bottom-bar{left:0;top:2999px;width:1200px;height:62px;background:var(--blue-dark);color:#dfe7f5;font-size:11px;display:flex;align-items:center;justify-content:center}
</style>
</head>
<body>

<header class="abs site-header">
  <div class="abs brand"><div class="brand-dot"></div><div class="brand-name">Quill Ridge Networks</div></div>
  <nav class="abs main-nav">
    <a class="active">HOME</a><a>ABOUT US</a><a>OUR SERVICES</a><a>BLOG</a><a>CONTACT US</a>
  </nav>
</header>

<section class="abs hero" role="img" aria-label="Photo of a smiling businessman in sunglasses working on a laptop on a beach"></section>
<div class="abs hero-title"><div class="l1">Linking Workplaces</div><div class="l2">as one for faster Web access</div></div>
<svg class="abs hero-arrow" style="left:42px" width="34" height="60" viewBox="0 0 34 60"><polyline points="30,2 4,30 30,58" fill="none" stroke="rgba(255,255,255,.6)" stroke-width="2"/></svg>
<svg class="abs hero-arrow" style="left:1124px" width="34" height="60" viewBox="0 0 34 60"><polyline points="4,2 30,30 4,58" fill="none" stroke="rgba(255,255,255,.6)" stroke-width="2"/></svg>

<h1 class="abs section-title" style="top:686px">Welcome to Quill Ridge Networks</h1>
<p class="abs intro">Sed ut perspiciatis unde omnis iste natus error sit voluptatem accusantium doloremque laudantium, totam rem aperiam, eaque ipsa quae ab illo inventore veritatis et quasi architecto beatae vitae dicta sunt explicabo. Nemo enim ipsam voluptatem quia voluptas sit aspernatur aut odit aut fugit, sed quia consequuntur magni dolores eos qui ratione voluptatem sequi nesciunt. Neque porro quisquam est, qui dolorem ipsum quia dolor sit amet, consectetur, adipisci velit.</p>

<article class="abs card" style="left:98px;top:851px">
  <div class="card-media" role="img" aria-label="Photo of a businessman with a laptop and phone on steps" style="background:linear-gradient(135deg,#8a8f96,#3c4a66)"></div>
  <h3>Business Solutions</h3>
  <p>Lorem ipsum dolor sit amet, consectetur adipiscing elit, sed do eiusmod tempor incididunt ut labore et dolore magna aliqua. Ut enim ad minim veniam.</p>
  <span class="more">Read more ›</span>
</article>
<article class="abs card" style="left:445px;top:851px">
  <div class="card-media" role="img" aria-label="Photo of hands using a tablet beside a laptop and coffee" style="background:linear-gradient(135deg,#b07a55,#d9d2c8 55%,#6d4a35)"></div>
  <h3>Home Connections</h3>
  <p>Lorem ipsum dolor sit amet, consectetur adipiscing elit, sed do eiusmod tempor incididunt ut labore et dolore magna aliqua. Ut enim ad minim veniam.</p>
  <span class="more">Read more ›</span>
</article>
<article class="abs card" style="left:790px;top:851px">
  <div class="card-media" role="img" aria-label="Illustration of glowing network links above a laptop" style="background:radial-gradient(circle at 50% 70%,#9fd4ff,#2a6fc9 45%,#0b2a66)"></div>
  <h3>Unlimited Internet</h3>
  <p>Lorem ipsum dolor sit amet, consectetur adipiscing elit, sed do eiusmod tempor incididunt ut labore et dolore magna aliqua. Ut enim ad minim veniam.</p>
  <span class="more">Read more ›</span>
</article>

<section class="abs connect">
  <h2 class="abs section-title">Connect Remote Businesses</h2>
  <div class="abs feature" style="left:98px;top:146px"><h4>Fibre and Microwave</h4><p>Sed ut perspiciatis unde omnis iste natus error sit voluptatem accusantium doloremque laudantium, totam rem aperiam, eaque ipsa quae ab illo inventore veritatis et quasi architecto beatae vitae dicta sunt explicabo.</p></div>
  <div class="abs feature" style="left:98px;top:309px"><h4>High Speed Internet</h4><p>Sed ut perspiciatis unde omnis iste natus error sit voluptatem accusantium doloremque laudantium, totam rem aperiam, eaque ipsa quae ab illo inventore veritatis et quasi architecto beatae vitae dicta sunt explicabo.</p></div>
  <div class="abs feature" style="left:765px;top:146px"><h4>Radio Technology</h4><p>Sed ut perspiciatis unde omnis iste natus error sit voluptatem accusantium doloremque laudantium, totam rem aperiam, eaque ipsa quae ab illo inventore veritatis et quasi architecto beatae vitae dicta sunt explicabo.</p></div>
  <div class="abs feature" style="left:765px;top:309px"><h4>Customer Support Center</h4><p>Sed ut perspiciatis unde omnis iste natus error sit voluptatem accusantium doloremque laudantium, totam rem aperiam, eaque ipsa quae ab illo inventore veritatis et quasi architecto beatae vitae dicta sunt explicabo.</p></div>

  <div class="abs icon-disc" style="left:459px;top:137px">
    <svg width="54" height="54" viewBox="0 0 54 54"><g fill="#2b5aa8"><rect x="18" y="8" width="5" height="14" rx="2" transform="rotate(45 27 27)"/><rect x="31" y="8" width="5" height="14" rx="2" transform="rotate(45 27 27)"/><rect x="13" y="20" width="28" height="16" rx="5" transform="rotate(45 27 27)"/><rect x="24.5" y="34" width="5" height="16" transform="rotate(45 27 27)"/></g></svg>
  </div>
  <div class="abs icon-disc" style="left:612px;top:137px">
    <svg width="54" height="54" viewBox="0 0 54 54"><g fill="#2b5aa8"><path d="M8 22h8l22-12v34L16 32H8z"/><rect x="14" y="32" width="7" height="12" rx="2"/><rect x="42" y="24" width="6" height="6" rx="2"/></g></svg>
  </div>
  <div class="abs icon-disc" style="left:459px;top:301px">
    <svg width="54" height="54" viewBox="0 0 54 54"><circle cx="27" cy="27" r="22" fill="#2b5aa8"/><path d="M14 18c6 2 8 8 14 7s4 8-2 10-4 9-8 6-6-12-4-23zM32 10c5 1 9 6 8 10-4 1-8-3-8-10z" fill="#fff"/></svg>
  </div>
  <div class="abs icon-disc" style="left:612px;top:301px">
    <svg width="54" height="54" viewBox="0 0 54 54"><circle cx="27" cy="27" r="22" fill="none" stroke="#2b5aa8" stroke-width="8"/><circle cx="27" cy="27" r="8" fill="none" stroke="#2b5aa8" stroke-width="3"/><g stroke="#fff" stroke-width="5"><line x1="9" y1="9" x2="19" y2="19"/><line x1="45" y1="9" x2="35" y2="19"/><line x1="9" y1="45" x2="19" y2="35"/><line x1="45" y1="45" x2="35" y2="35"/></g></svg>
  </div>
</section>

<div class="abs carrier-head"><div class="mark"></div><div><h2>Carrier Partners &amp; Technologies</h2><div class="sub">Nemo enim ipsam voluptatem quia voluptas sit</div></div></div>
<div class="abs carrier-text">
  <p>Lorem ipsum dolor sit amet, consectetur adipiscing elit, sed do eiusmod tempor incididunt ut labore et dolore magna aliqua. Ut enim ad minim veniam, quis nostrud exercitation ullamco laboris nisi ut aliquip ex ea commodo consequat. Duis aute irure dolor in reprehenderit in voluptate velit esse cillum dolore eu fugiat nulla pariatur. Excepteur sint occaecat cupidatat non proident.</p>
  <p>Lorem ipsum dolor sit amet, consectetur adipiscing elit, sed do eiusmod tempor incididunt ut labore et dolore magna aliqua. Ut enim ad minim veniam, quis nostrud exercitation</p>
</div>
<div class="abs btn-blue">READ MORE</div>
<div class="abs video" role="img" aria-label="Illustration of a woman lying on the floor with a laptop, surrounded by media icons, with a play button"></div>
<svg class="abs" style="left:866px;top:1912px" width="50" height="34" viewBox="0 0 50 34"><rect width="50" height="34" rx="7" fill="#111"/><polygon points="20,9 33,17 20,25" fill="#fff"/></svg>
<div class="abs video-shadow"></div>

<div class="abs partner" style="left:98px"><span></span></div>
<div class="abs partner" style="left:265px"><span></span></div>
<div class="abs partner" style="left:435px"><span></span></div>
<div class="abs partner" style="left:604px"><span></span></div>
<div class="abs partner" style="left:773px"><span></span></div>
<div class="abs partner" style="left:943px"><span></span></div>

<section class="abs booking" role="img" aria-label="Dark photo of people working at a desk with laptops">
  <h2 class="abs section-title">Service Booking Requests</h2>
</section>
<div class="abs field" style="left:190px;top:2456px">Your first name</div>
<div class="abs field" style="left:473px;top:2456px">Business Address</div>
<div class="abs field" style="left:755px;top:2456px">Business Phone Number</div>
<div class="abs field" style="left:190px;top:2513px">Your mobile</div>
<div class="abs field" style="left:473px;top:2513px">Number of Staff</div>
<div class="abs field" style="left:755px;top:2513px">Current Internet connection</div>
<div class="abs field" style="left:190px;top:2571px">Speed</div>
<div class="abs field" style="left:473px;top:2571px">Comments</div>
<div class="abs field btn-orange" style="left:755px;top:2571px">Booking Requests ⊙</div>

<footer class="abs site-footer"></footer>
<div class="abs f-col" style="left:98px;top:2766px;width:260px">
  <h5>Join our Newsletter</h5>
  <p>Excepteur sint occaecat cupidatat non proident, sunt in culpa qui</p>
  <div class="input">Enter Name</div>
  <div class="btn-sub">Subscribe</div>
</div>
<div class="abs f-col" style="left:424px;top:2760px;width:260px">
  <h5>Contacts Us</h5>
  <div class="contact-row"><svg width="12" height="16" viewBox="0 0 12 16"><path d="M6 0a6 6 0 0 0-6 6c0 4 6 10 6 10s6-6 6-10a6 6 0 0 0-6-6z" fill="#999"/><circle cx="6" cy="6" r="2" fill="#f4f4f4"/></svg><p>Harlow Vale, New South Wales<br>Australia</p></div>
  <div class="contact-row"><svg width="12" height="14" viewBox="0 0 12 14"><path d="M2 0l3 3-1.5 2c1 2 2 3 4 4L9 7.5l3 3L10 13C5 12 0 7 0 2z" fill="#999"/></svg><p>Phone: (555) 014-2290</p></div>
  <div class="contact-row"><svg width="13" height="10" viewBox="0 0 13 10"><rect width="13" height="10" fill="#999"/><polyline points="0,0 6.5,6 13,0" fill="none" stroke="#f4f4f4"/></svg><p>info@quillridgenetworks.com</p></div>
  <div class="socials"><span></span><span></span><span></span><span></span><span></span></div>
</div>
<div class="abs f-col" style="left:748px;top:2760px;width:160px">
  <h5>Quick Links</h5>
  <ul><li>Home</li><li>About Us</li><li>Contact Us</li><li>Services</li><li>Case Studies</li><li>Blog</li></ul>
</div>
<div class="abs foot-brand"><div class="brand-dot"></div><div class="brand-name">Quill Ridge Networks</div></div>
<div class="abs bottom-bar">©2015 - 2016 Quill Ridge Networks, All Rights Reserved.</div>

</body>
</html>
```